TG - management consultant

Business card - contemporary design

Front info
Thomas Galloway

(Address not necessary)
PO Box 7324
Belmont, CA 94002

(650) 482-3719
tg@thomasgallo.wy

Chatter: tgq287
Friendlist: /Thomas.Galloway
Worknet: /in/thomasgalloway

Back or Front
www.thomasgalloway.net
Facilitation & coaching, change management, strategic partnerships, business improvement

Target Market(s)

High tech businesses - mostly startups in Silicon Valley

Industry/Entity Type

Business

Font styles to use
Sans Serif

Colors

Designer to choose colors to be used in the design.

```html
<!DOCTYPE html>
<html lang="en">
<head>
<meta charset="UTF-8">
<title>Thomas Galloway – Business Cards</title>
<link href="https://fonts.googleapis.com/css2?family=Jost:wght@600&family=Arimo:wght@400;700&display=swap" rel="stylesheet">
<style>
  :root {
    --backdrop: #d3ecf1;
    --card-black: #000000;
    --ink-white: #ffffff;
    --ink-black: #000000;
  }
  * { margin: 0; padding: 0; box-sizing: border-box; }
  html, body {
    width: 1100px;
    height: 1200px;
    overflow: hidden;
    background: var(--backdrop);
  }
  .canvas {
    position: relative;
    width: 1100px;
    height: 1200px;
  }
  .card {
    position: absolute;
    left: 120px;
    width: 860px;
    height: 490px;
    background: var(--card-black);
    color: var(--ink-white);
    font-family: "Arimo", Arial, sans-serif;
    box-shadow: 0 18px 40px rgba(40, 80, 90, 0.25);
  }
  .card--services { top: 70px; }
  .card--contact { top: 640px; }

  .name-block {
    position: absolute;
    left: 145px;
    top: 20px;
    width: 270px;
    height: 200px;
    background: var(--ink-white);
  }
  .name-first,
  .name-last {
    position: absolute;
    font-family: "Jost", "Futura", sans-serif;
    font-weight: 600;
    font-size: 64px;
    line-height: 1;
    letter-spacing: -0.5px;
    white-space: nowrap;
  }
  .name-first {
    left: 14px;
    bottom: 14px;
    color: var(--ink-black);
  }
  .name-last {
    left: 430px;
    top: 160px;
    color: var(--ink-white);
  }
  .job-title {
    position: absolute;
    left: 430px;
    top: 232px;
    font-weight: 700;
    font-size: 25px;
    white-space: nowrap;
  }
  .services {
    position: absolute;
    left: 430px;
    top: 272px;
    list-style: none;
    font-size: 23px;
    line-height: 34px;
    white-space: nowrap;
  }
  .services li::before { content: "* "; }
  .website {
    position: absolute;
    right: 70px;
    bottom: 34px;
    font-weight: 700;
    font-size: 22px;
    white-space: nowrap;
  }
  .social {
    position: absolute;
    left: 55px;
    bottom: 40px;
    font-weight: 700;
    font-size: 22px;
    line-height: 29px;
    white-space: nowrap;
  }
  .direct {
    position: absolute;
    right: 90px;
    bottom: 40px;
    font-weight: 700;
    font-size: 22px;
    line-height: 29px;
    white-space: nowrap;
  }
</style>
</head>
<body>
<main class="canvas">

  <section class="card card--services" aria-label="Card with services">
    <div class="name-block"><span class="name-first">Thomas</span></div>
    <span class="name-last">Galloway</span>
    <p class="job-title">Management Consultant</p>
    <ul class="services">
      <li>Facilitation &amp; coaching</li>
      <li>Change management</li>
      <li>Strategic partnerships</li>
      <li>Business improvement</li>
    </ul>
    <p class="website">www.thomasgalloway.net</p>
  </section>

  <section class="card card--contact" aria-label="Card with contact details">
    <div class="name-block"><span class="name-first">Thomas</span></div>
    <span class="name-last">Galloway</span>
    <p class="job-title">Management Consultant</p>
    <div class="social">
      <p>Chatter: tgq287</p>
      <p>Friendlist: /Thomas.Galloway</p>
      <p>Worknet: /in/thomasgalloway</p>
    </div>
    <div class="direct">
      <p>(650) 482-3719</p>
      <p>tg@thomasgallo.wy</p>
    </div>
  </section>

</main>
</body>
</html>
```